Volna Beauty Mobile App Design

We need an app design for a new on-demand beauty service app called Volna Beauty. We help customers find and book beauty services on-demand (within 48 hours) or into the future. We would like to see designs that are clean and include the logs colors with dark and light shades of grey.
Design should be clean and modern yet showcase that this is a beauty app. It should beautiful and artful as well.
One set of mockups are attached, another set exists.
Competitors include trimquay.com or lustorio.com
Key: You can change the mockups to be best suited for functionality and design. These are here for content only.
Updates
The designs so far look great! Can you please design the portfolio screen for me to see navigation and a registration page to see your idea of textbox and buttons.
Industry/Entity Type
It Service
Look and feel
Each slider illustrates characteristics of the customer's brand and the style your logo design should communicate.

```html
<!DOCTYPE html>
<html lang="en">
<head>
<meta charset="utf-8">
<title>Volna Beauty – App Screens</title>
<link rel="stylesheet" href="https://fonts.googleapis.com/css2?family=Roboto:wght@300;400;500&display=swap">
<style>
  :root {
    --purple: #6a0dad;
    --purple-deep: #642c86;
    --purple-soft: #744096;
    --ink: #111111;
    --grey-text: #6d6d6d;
    --field: #c9c9c9;
    --field-text: #8e8e8e;
    --status-grey: #cfcfcf;
    --white: #ffffff;
    --canvas: #ffffff;
  }
  * { box-sizing: border-box; margin: 0; padding: 0; }
  html, body { width: 1200px; height: 1028px; overflow: hidden; background: var(--canvas); }
  body { position: relative; font-family: "Roboto", "Helvetica Neue", Arial, sans-serif; color: var(--ink); }

  .screen { position: absolute; top: 169px; width: 367px; height: 639px; overflow: hidden; }
  .screen--splash { left: 0; }
  .screen--menu { left: 403px; }
  .screen--login { left: 800px; }

  .soft-bg { background: radial-gradient(ellipse 75% 50% at 50% 32%, #ffffff 0%, #eeeeee 50%, #c4c4c4 100%); }

  .status-bar { position: absolute; top: 0; left: 0; right: 0; height: 24px; display: flex; align-items: center; padding: 0 6px; font-size: 14px; background: var(--white); }
  .screen--splash .status-bar { background: var(--status-grey); height: 27px; font-size: 15px; }
  .status-bar .carrier { display: flex; align-items: center; gap: 4px; }
  .status-bar .time { position: absolute; left: 50%; transform: translateX(-50%); font-weight: 500; }
  .status-bar .right { margin-left: auto; display: flex; align-items: center; gap: 5px; }

  .nav-bar { position: absolute; top: 24px; left: 0; right: 0; height: 50px; background: #fafafa; border-bottom: 1px solid #b9b9b9; display: flex; align-items: center; justify-content: center; }
  .nav-bar .title { font-size: 19px; font-weight: 400; }
  .nav-bar .brand-title { color: var(--purple); font-size: 21px; font-weight: 300; }
  .nav-bar .nav-icon { position: absolute; left: 10px; top: 14px; }

  .brand { position: absolute; left: 0; right: 0; text-align: center; }
  .brand .name { color: var(--purple); font-size: 38px; font-weight: 300; line-height: 1; }
  .brand .tagline { font-size: 12px; color: var(--grey-text); margin-top: 10px; }
  .screen--splash .brand { top: 328px; }
  .screen--login .brand { top: 252px; }

  .drawer { position: absolute; top: 74px; left: 0; width: 294px; bottom: 0; border-right: 1px solid #4d1a70; }
  .drawer-profile { height: 290px; background: linear-gradient(170deg, #6a3390, var(--purple-deep)); text-align: center; padding-top: 50px; }
  .avatar { width: 168px; height: 168px; border-radius: 50%; margin: 0 auto; background: radial-gradient(circle at 50% 45%, #d9b49a 0%, #8a6040 60%, #4a3322 100%); }
  .profile-name { color: var(--white); font-size: 22px; font-weight: 300; margin-top: 28px; }
  .drawer-menu { position: absolute; top: 290px; left: 0; right: 0; bottom: 0; background: radial-gradient(ellipse at 90% 10%, #7c4a9c, var(--purple-soft) 40%, #66308a 100%); padding: 69px 30px 0 25px; list-style: none; }
  .drawer-menu li { color: var(--white); font-size: 22px; font-weight: 300; height: 37.5px; line-height: 34px; border-bottom: 1px solid rgba(255,255,255,0.6); }
  .drawer-menu li:last-child { border-bottom: none; }
  .content-peek { position: absolute; top: 74px; left: 294px; right: 0; bottom: 0; background: linear-gradient(90deg, #d4d4d4, #b9b9b9); }

  .login-form { position: absolute; top: 382px; left: 22px; width: 324px; }
  .field { height: 36px; background: var(--field); border-radius: 2px; color: var(--field-text); font-size: 16px; display: flex; align-items: center; justify-content: center; margin-bottom: 23px; }
  .actions { display: flex; justify-content: space-between; margin-top: -3px; }
  .btn { width: 154px; height: 37px; border-radius: 2px; display: flex; align-items: center; justify-content: center; font-size: 16px; }
  .btn--register { background: var(--white); color: #9a9a9a; }
  .btn--login { background: var(--purple); color: var(--white); }
</style>
</head>
<body>

<section class="screen screen--splash soft-bg">
  <div class="status-bar">
    <span class="carrier">●●●●○ KESTA
      <svg width="18" height="13" viewBox="0 0 18 13"><path d="M9 12l2.5-3a3.5 3.5 0 0 0-5 0z M3.5 6.5a8 8 0 0 1 11 0l-1.5 1.7a5.7 5.7 0 0 0-8 0z M1 3.6a11.5 11.5 0 0 1 16 0l-1.4 1.6a9.4 9.4 0 0 0-13.2 0z" fill="#111"/></svg>
    </span>
    <span class="right">
      <svg width="9" height="14" viewBox="0 0 9 14"><path d="M1 4l6 6-3 3V1l3 3-6 6" fill="none" stroke="#444" stroke-width="1.3"/></svg>
      82%
      <svg width="34" height="14" viewBox="0 0 34 14"><rect x="0.5" y="1.5" width="26" height="11" rx="2" fill="none" stroke="#111"/><rect x="2" y="3" width="20" height="8" fill="#111"/><rect x="27.5" y="5" width="2" height="4" fill="#111"/><path d="M31 2l-2 6h2l-1 5 3-7h-2l1-4z" fill="#111"/></svg>
    </span>
  </div>
  <div class="brand">
    <div class="name">Volna Beauty</div>
    <div class="tagline">On Demand Beauty Services</div>
  </div>
</section>

<section class="screen screen--menu">
  <div class="status-bar">
    <span class="carrier">●●●○○ KESTA
      <svg width="16" height="12" viewBox="0 0 18 13"><path d="M9 12l2.5-3a3.5 3.5 0 0 0-5 0z M3.5 6.5a8 8 0 0 1 11 0l-1.5 1.7a5.7 5.7 0 0 0-8 0z M1 3.6a11.5 11.5 0 0 1 16 0l-1.4 1.6a9.4 9.4 0 0 0-13.2 0z" fill="#111"/></svg>
    </span>
    <span class="time">4:21 PM</span>
    <span class="right">
      <svg width="9" height="13" viewBox="0 0 9 14"><path d="M1 4l6 6-3 3V1l3 3-6 6" fill="none" stroke="#444" stroke-width="1.3"/></svg>
      100%
      <svg width="30" height="13" viewBox="0 0 30 13"><rect x="0.5" y="1" width="25" height="11" rx="2" fill="none" stroke="#111"/><rect x="2" y="2.5" width="22" height="8" fill="#111"/><rect x="26.5" y="4.5" width="2" height="4" fill="#111"/></svg>
    </span>
  </div>
  <header class="nav-bar">
    <svg class="nav-icon" width="24" height="20" viewBox="0 0 24 20" aria-label="Menu"><rect y="0" width="24" height="4" fill="var(--purple)"/><rect y="8" width="24" height="4" fill="var(--purple)"/><rect y="16" width="24" height="4" fill="var(--purple)"/></svg>
    <span class="brand-title">Volna Beauty</span>
  </header>
  <div class="content-peek"></div>
  <nav class="drawer">
    <div class="drawer-profile">
      <div class="avatar" role="img" aria-label="Profile photo of the signed-in beauty professional"></div>
      <div class="profile-name">Marina Kessel</div>
    </div>
    <ul class="drawer-menu">
      <li>Find work</li>
      <li>My Account</li>
      <li>Share</li>
      <li>Logout</li>
    </ul>
  </nav>
</section>

<section class="screen screen--login soft-bg">
  <div class="status-bar">
    <span class="carrier">●●●○○ KESTA
      <svg width="16" height="12" viewBox="0 0 18 13"><path d="M9 12l2.5-3a3.5 3.5 0 0 0-5 0z M3.5 6.5a8 8 0 0 1 11 0l-1.5 1.7a5.7 5.7 0 0 0-8 0z M1 3.6a11.5 11.5 0 0 1 16 0l-1.4 1.6a9.4 9.4 0 0 0-13.2 0z" fill="#111"/></svg>
    </span>
    <span class="time">4:21 PM</span>
    <span class="right">
      <svg width="9" height="13" viewBox="0 0 9 14"><path d="M1 4l6 6-3 3V1l3 3-6 6" fill="none" stroke="#444" stroke-width="1.3"/></svg>
      100%
      <svg width="30" height="13" viewBox="0 0 30 13"><rect x="0.5" y="1" width="25" height="11" rx="2" fill="none" stroke="#111"/><rect x="2" y="2.5" width="22" height="8" fill="#111"/><rect x="26.5" y="4.5" width="2" height="4" fill="#111"/></svg>
    </span>
  </div>
  <header class="nav-bar">
    <svg class="nav-icon" width="14" height="22" viewBox="0 0 14 22" aria-label="Back"><path d="M12 2L3 11l9 9" fill="none" stroke="var(--purple)" stroke-width="3"/></svg>
    <span class="title">Login</span>
  </header>
  <div class="brand">
    <div class="name">Volna Beauty</div>
    <div class="tagline">On Demand Beauty Services</div>
  </div>
  <form class="login-form">
    <div class="field">email</div>
    <div class="field">password</div>
    <div class="actions">
      <div class="btn btn--register">register</div>
      <div class="btn btn--login">login</div>
    </div>
  </form>
</section>

</body>
</html>
```